A WEBSITE FOR A JEWELLERY RETAIL STORE WITH A SHOPPING CART, AND ABILITY TO ORDER ONLINE.

I require a website with a shopping cart.

We sell MAINLY diamond jewellery (such as rings etc). I need it to be simple to change prices with only a few buttons, as the price fluctuates due to the US Dollar.

We are a diamond wholesaler, selling directly to the public, so we guarantee the lowest prices in Australia.

There is also a link to current inventory that will need to be uploaded to the site.

This could be an ongoing job, where you will be paid weekly to maintain and update the website if you wish.

Target Market(s)

People getting engaged, and wanting to buy a diamond ring.

Number of Pages Required

5+ page

Colors

Designer to choose colors to be used in the design.

Requirements
Must have
• elegant.
• modern.
• professional.
• SHOPPING CART.
• ABILITY TO SEARCH FOR LOOSE DIAMONDS (LINK THAT NEEDS TO BE EMBEDDED WILL BE SENT WHICH SHOWS CURRENT STOCK).
• ENGAGEMENT RINGS
• WEDDING RINGS
• DIAMOND EARRINGS
• DIAMOND PENDANTS
• LOOSE DIAMONDS.
• SALE ITEMS.
• OTHER JEWELLERY.
• EDUCATION
• WISH LIST
• CART.
Nice to have
• a good place to look for inspiration on pages is https://www.lumenvael.example.
• YOU MAY VISIT OUR FACEBOOK PAGE AT.
• HTTP://WWW.SOCIALPAGE.EXAMPLE/QUILLSTONEJEWELLERS
Should not have
• We don't want it too busy.

```html
<!DOCTYPE html>
<html lang="en">
<head>
<meta charset="utf-8">
<title>Quillstone Jewellers – Home</title>
<link href="https://fonts.googleapis.com/css2?family=Open+Sans:wght@400;600&family=Playfair+Display:wght@700&display=swap" rel="stylesheet">
<style>
:root{
  --stage:#dcdcdc;
  --ink:#111111;
  --black:#000000;
  --white:#ffffff;
  --bar:#e6e6e6;
  --muted:#9a9a9a;
  --red:#e03a2f;
  --yellow:#f6b51e;
  --orange:#f39a1f;
  --hero-a:#4a4a4a;
  --hero-b:#141414;
}
*{box-sizing:border-box;margin:0;padding:0}
html,body{width:1200px;height:1200px;overflow:hidden}
body{background:var(--stage);font-family:"Open Sans",Arial,sans-serif;color:var(--ink);position:relative}
.page{position:absolute;left:453px;top:19px;width:600px;height:2370px;background:var(--white);transform:scale(.49);transform-origin:0 0;overflow:hidden}
.abs{position:absolute}
/* top bar */
.topbar{left:0;top:0;width:600px;height:30px;background:var(--white);border-bottom:1px solid #ddd;font-size:8px;display:flex;align-items:center;padding:0 40px;gap:12px}
.topbar .social{display:flex;gap:6px}
.topbar .social span{width:7px;height:7px;background:var(--ink);border-radius:50%}
.topbar .help{font-weight:600}
.topbar .links{margin-left:auto;display:flex;gap:22px;align-items:center}
/* nav */
.nav{left:0;top:30px;width:600px;height:40px;background:var(--bar);display:flex;align-items:center;padding:0 40px}
.brand{display:flex;align-items:center;gap:6px;font-size:13px;line-height:1;color:var(--ink);letter-spacing:1px}
.brand .mark{width:12px;height:12px;background:var(--ink)}
.brand small{display:block;font-size:6px;letter-spacing:4px;margin-top:2px}
.menu{margin-left:auto;display:flex;gap:18px;font-size:8px;font-weight:600}
.menu .active{color:var(--red)}
.dropdown{left:282px;top:70px;width:82px;background:var(--white);font-size:7px;text-align:center;font-weight:600;box-shadow:0 2px 4px rgba(0,0,0,.3)}
.dropdown div{padding:3px 0}
.dropdown .on{background:var(--red);color:var(--white)}
/* hero */
.hero{left:0;top:70px;width:600px;height:285px;background:radial-gradient(ellipse at 68% 45%,#6b5a3a 0%,var(--hero-a) 35%,var(--hero-b) 100%)}
.hero h1{position:absolute;left:45px;top:60px;font-family:"Playfair Display",Georgia,serif;font-size:34px;color:var(--white)}
.hero p{position:absolute;left:45px;top:112px;font-size:9px;color:var(--white);width:260px;line-height:1.3}
.btn{display:inline-block;font-size:8px;padding:5px 12px;border-radius:3px;color:var(--white)}
.btn.yellow{background:var(--yellow)}
.btn.ghost{border:1.5px solid var(--white)}
.btn.orange{background:var(--orange)}
.btn.red{background:var(--red)}
.hero .actions{position:absolute;left:45px;top:150px;display:flex;gap:6px}
/* tiles */
.photo-light{background:radial-gradient(circle at 50% 50%,#f4f4f4 0%,#d9d9d9 70%,#ffffff 100%)}
.tile-dark{background:var(--black);color:var(--white);padding:30px 22px;font-size:7px;line-height:1.35}
.tile-dark h3{font-size:11px;font-weight:400;margin-bottom:10px}
.tag{position:absolute;top:10px;left:10px;width:22px;height:10px;background:var(--yellow);border-radius:2px}
/* sale */
.sale{left:0;top:692px;width:600px;height:210px;background:radial-gradient(ellipse at 45% 45%,#7a3a08 0%,#2a1205 35%,var(--black) 70%);color:var(--white);text-align:center}
.sale h2{font-weight:400;font-size:24px;margin-top:58px;letter-spacing:1px}
.sale p{font-size:11px;margin:4px 0 8px}
.sale .btn{border:1.5px solid var(--white);font-size:10px;padding:2px 8px}
/* featured */
.section-title{font-size:15px;font-weight:400;color:#333}
.card{width:120px;height:220px;border:1px solid #ccc;background:var(--white);padding:4px}
.card .img{height:105px}
.card b{display:block;font-size:7px;font-weight:600;margin:6px 0 3px}
.card p{font-size:6px;color:#555;line-height:1.3}
.card .price{font-size:6px;margin:6px 0}
.card .row{display:flex;justify-content:space-between;align-items:center}
.card .mini{width:22px;height:9px;background:var(--orange)}
.card .ic{width:9px;height:7px;background:#777}
/* loose */
.loose{left:0;top:1222px;width:600px;height:205px;background:var(--black);color:var(--white);text-align:center}
.loose h2{font-size:15px;font-weight:400;margin-top:32px}
.loose p{font-size:9px;width:380px;margin:8px auto 0;line-height:1.3}
.search{width:250px;height:22px;background:var(--white);margin:12px auto 0;display:flex;align-items:center;justify-content:space-between;padding:0 8px;font-size:8px;color:var(--muted)}
/* education */
.edu{left:0;top:1427px;width:600px;height:225px;background:linear-gradient(90deg,#2a2a2a 0%,#3c3c3c 45%,#6a625a 100%);color:var(--white)}
.edu h2{position:absolute;left:45px;top:52px;font-size:15px;font-weight:400}
.edu p{position:absolute;left:45px;top:80px;width:290px;font-size:9px;line-height:1.25}
.edu .btn{position:absolute;left:305px;top:150px;font-size:10px;padding:5px 10px}
/* best */
.promo{background:linear-gradient(#3d3d3d,#262626);color:var(--white);text-align:center;font-size:15px;padding-top:30px;line-height:1.6}
.promo .btn{font-size:10px;padding:2px 16px}
.framed{border:1px solid #3f7a6a}
/* drive */
.drive{left:0;top:1960px;width:600px;height:180px;background:radial-gradient(ellipse at 50% 70%,#7a7a7a 0%,#3a3a3a 45%,#1a1a1a 100%);color:var(--white);text-align:center}
.drive h2{font-size:15px;font-weight:600;margin-top:40px}
.drive p{font-size:7px;margin-top:4px}
.drive .btn{margin-top:30px;border:1.5px solid var(--white);font-size:7px;padding:2px 6px;background:#222}
/* footer */
.footer{left:0;top:2140px;width:600px;height:230px;background:var(--black);color:var(--white);font-size:7px}
.footer h4{font-size:10px;font-weight:400;margin-bottom:14px}
.footer .col{position:absolute;top:55px;line-height:1.4}
.footer .mail{width:165px;height:15px;background:var(--white);color:var(--muted);padding:3px 4px;font-size:6px}
.footer .dots{display:flex;gap:26px;margin-top:18px;padding-left:35px}
.footer .dots span{width:14px;height:14px;border:1.5px solid var(--white);border-radius:50%}
.footer .copy{position:absolute;left:0;right:0;bottom:12px;text-align:center;border-top:1px solid #333;margin:0 50px;padding-top:14px}
</style>
</head>
<body>
<main class="page">
  <header class="abs topbar">
    <div class="social"><span></span><span></span><span></span></div>
    <div class="help">Need Help: Call+100555018</div>
    <nav class="links"><span>My Account</span><span>Blog</span><span>Company</span><span>Login</span>
      <svg width="12" height="9" viewBox="0 0 12 9"><path d="M0 1h2l2 5h6l1.5-4H3" fill="none" stroke="#111" stroke-width="1.2"/><circle cx="5" cy="8" r="1" fill="#111"/><circle cx="9" cy="8" r="1" fill="#111"/></svg>
    </nav>
  </header>

  <div class="abs nav">
    <div class="brand"><span class="mark"></span><div>QUILLSTONE<small>JEWELLERS</small></div></div>
    <nav class="menu"><span>HOME</span><span class="active">COLLECTION ▾</span><span>ON SALE</span><span>EDUCATION</span><span>CONTACT</span></nav>
  </div>

  <section class="abs hero" role="img" aria-label="Gold diamond ring set on dark stone">
    <h1>Jewellers</h1>
    <p>LOREM IPSUM DOLOR SIT AMET, CONSECTETUR ADIPISCING ELIT, SED.</p>
    <div class="actions"><span class="btn yellow">SHOP NOW</span><span class="btn ghost">READ MORE</span></div>
  </section>

  <div class="abs dropdown"><div>DIAMONDS</div><div class="on">WEDDING</div><div>ENGAGEMENT RING</div><div>JEWELARY</div></div>

  <div class="abs photo-light" style="left:85px;top:300px;width:212px;height:205px" role="img" aria-label="Gold halo diamond engagement ring"></div>
  <div class="abs tile-dark" style="left:297px;top:300px;width:225px;height:205px">
    <span class="tag"></span>
    <h3>ENGAGEMENT</h3>
    <p>Lorem ipsum dolor sit amet, consectetur adipiscing elit, sed do eiusmod tempor incididunt ut labore et dolore magna aliqua.</p>
    <p style="margin-top:14px;text-align:center"><span class="btn red">MORE</span></p>
  </div>
  <div class="abs tile-dark" style="left:85px;top:507px;width:212px;height:185px">
    <span class="tag" style="left:auto;right:10px"></span>
    <h3>Jewellery</h3>
    <p>Lorem ipsum dolor sit amet, consectetur adipiscing elit, sed do eiusmod tempor incididunt ut labore et dolore magna aliqua.</p>
    <p style="margin-top:14px"><span class="btn yellow">MORE</span></p>
  </div>
  <div class="abs photo-light" style="left:297px;top:507px;width:225px;height:185px" role="img" aria-label="White gold solitaire diamond ring"></div>

  <section class="abs sale" role="img" aria-label="Sale banner with amber jewellery glow">
    <h2>SAVE 50% OFF</h2>
    <p>Shop our Year-End sale - upto 50%</p>
    <span class="btn">Shop Now</span>
  </section>

  <h2 class="abs section-title" style="left:75px;top:932px">Featured Product</h2>
  <div class="abs card" style="left:40px;top:970px"><div class="img photo-light" role="img" aria-label="Oval diamond engagement ring"></div><b>Engagement Ring</b><p>Lorem ipsum dolor sit amet, consectetur adipiscing elit sed.</p><div class="price">$ 99.00</div><div class="row"><span class="mini"></span><span class="ic"></span><span class="ic"></span></div></div>
  <div class="abs card" style="left:172px;top:970px"><div class="img photo-light" role="img" aria-label="Diamond wedding ring"></div><b>Wedding Ring</b><p>Lorem ipsum dolor sit amet, consectetur adipiscing elit sed.</p><div class="price">$ 99.00</div><div class="row"><span class="mini"></span><span class="ic"></span><span class="ic"></span></div></div>
  <div class="abs card" style="left:302px;top:970px;box-shadow:0 0 6px rgba(0,0,0,.4)"><div class="img photo-light" role="img" aria-label="Gold halo diamond ring"></div><b>Gold Ring</b><p>Lorem ipsum dolor sit amet, consectetur adipiscing elit sed.</p><div class="price">$ 99.00</div><div class="row"><span class="mini"></span><span class="ic"></span><span class="ic"></span></div></div>
  <div class="abs card" style="left:432px;top:970px"><div class="img photo-light" role="img" aria-label="Oval diamond ring"></div><b>Diamond Ring</b><p>Lorem ipsum dolor sit amet, consectetur adipiscing elit sed.</p><div class="price">$ 99.00</div><div class="row"><span class="mini"></span><span class="ic"></span><span class="ic"></span></div></div>

  <section class="abs loose">
    <h2>Loose Diamonds</h2>
    <p>Lorem ipsum dolor sit amet, consectetur adipiscing elit, sed do eiusmod tempor incididunt ut labore et dolore magna aliqua.</p>
    <div class="search"><span>Search</span>
      <svg width="9" height="9" viewBox="0 0 9 9"><circle cx="3.8" cy="3.8" r="2.8" fill="none" stroke="#111" stroke-width="1.2"/><path d="M6 6l2.5 2.5" stroke="#111" stroke-width="1.3"/></svg>
    </div>
  </section>

  <section class="abs edu" role="img" aria-label="Jeweller working at a bench">
    <h2>EDUCATION CENTER</h2>
    <p>Our education center contains useful tips on how to buy diamonds, engagement rings, wedding bands, and finding that perfect gift for someone you love.</p>
    <span class="btn orange">Design your own Ring</span>
  </section>

  <h2 class="abs section-title" style="left:82px;top:1690px;font-size:14px">Our Best Selling items</h2>
  <div class="abs promo" style="left:42px;top:1745px;width:165px;height:160px">Diamond Ring<br>20% off<br><span class="btn orange">View</span></div>
  <div class="abs photo-light framed" style="left:217px;top:1745px;width:163px;height:160px" role="img" aria-label="Gold halo diamond ring"></div>
  <div class="abs photo-light" style="left:390px;top:1745px;width:165px;height:160px;border:1px solid #999" role="img" aria-label="Pavé diamond ring"></div>

  <section class="abs drive" role="img" aria-label="Diamond ring on dark surface">
    <h2>DRIVE YOUR OWN DESIGN</h2>
    <p>OFFERING VARIOUS STYLES AND VALUABLE METAL OPTIONS.</p>
    <span class="btn">GET STARTED</span>
  </section>

  <footer class="abs footer">
    <div class="col" style="left:57px"><h4>About us.</h4>Lorem ipsum dolor sit amet,<br>Lorem ipsum dolor sit amet,<br>ipsum dolor sit amet.</div>
    <div class="col" style="left:242px;text-align:center"><h4>PHONE SUPPORT</h4>24/7 Call us now<br>+100555019</div>
    <div class="col" style="left:390px"><h4 style="padding-left:38px">NEWSLETTER</h4><div class="mail">Enter Your Email</div><div class="dots"><span></span><span></span><span></span></div></div>
    <div class="copy">Copyright @ 2018. All Rights Reserved.</div>
    <svg class="abs" style="right:30px;bottom:14px" width="10" height="6" viewBox="0 0 10 6"><path d="M0 6L5 0l5 6z" fill="#fff"/></svg>
  </footer>
</main>
</body>
</html>
```